First Aid Training business needs business card design

We would like a double sided business card designed for a first aid training business - Brindlewood First Aid. We provide first aid training and , WHS (work, health and safety) training.

The attached word document contains the key information we would like on each side of the business card.

Final design needs to be delivered in print ready format, along with the original file.

```html
<!DOCTYPE html>
<html lang="en">
<head>
<meta charset="utf-8">
<title>Brindlewood First Aid – Business Card</title>
<link rel="stylesheet" href="https://fonts.googleapis.com/css2?family=Open+Sans:wght@400;700&display=swap">
<style>
  :root {
    --red: #ee1c24;
    --grey: #808080;
    --ink: #1a1a1a;
    --paper: #ffffff;
    --page: #ffffff;
    --edge: #2b2b2b;
  }
  * { margin: 0; padding: 0; box-sizing: border-box; }
  html, body {
    width: 1047px;
    height: 1200px;
    overflow: hidden;
    background: var(--page);
    font-family: "Open Sans", Arial, sans-serif;
  }
  .sheet { position: relative; width: 1047px; height: 1200px; }
  .card {
    position: absolute;
    left: 122px;
    width: 809px;
    height: 473px;
    background: var(--paper);
    border: 1px solid var(--edge);
    overflow: hidden;
    box-shadow: 2px 5px 8px rgba(0,0,0,0.25);
  }
  .card--front { top: 107px; }
  .card--back { top: 630px; }
  .card__decor { position: absolute; top: 0; left: 0; width: 809px; height: 473px; }

  /* Front */
  .brand {
    position: absolute;
    left: 64px;
    top: 62px;
    display: flex;
    align-items: center;
    gap: 18px;
  }
  .brand__dot {
    width: 72px; height: 72px;
    border-radius: 50%;
    background: var(--red);
    flex: none;
  }
  .brand__name {
    font-weight: 700;
    font-size: 29px;
    line-height: 1.1;
    color: var(--ink);
    text-transform: uppercase;
    letter-spacing: 0.5px;
  }
  .contact { position: absolute; left: 62px; top: 230px; color: var(--ink); }
  .contact__name {
    font-weight: 700;
    font-size: 30px;
    color: var(--red);
    line-height: 1;
  }
  .contact__phone {
    margin-top: 47px;
    font-weight: 700;
    font-size: 21px;
    line-height: 1;
  }
  .contact__lines {
    margin-top: 21px;
    font-size: 22px;
    line-height: 30px;
  }

  /* Back */
  .offer { position: absolute; left: 359px; top: 86px; }
  .offer__title {
    font-weight: 700;
    font-size: 26px;
    line-height: 31px;
    letter-spacing: 1.2px;
    text-transform: uppercase;
  }
  .offer__title--red { color: var(--red); }
  .offer__title--grey { color: var(--grey); }
  .benefits { list-style: none; margin-top: 22px; }
  .benefits li {
    position: relative;
    padding-left: 24px;
    font-size: 22px;
    line-height: 36px;
    color: var(--ink);
  }
  .benefits li::before {
    content: "";
    position: absolute;
    left: 0; top: 13px;
    width: 10px; height: 10px;
    background: var(--red);
  }
  .services {
    margin-top: 34px;
    font-weight: 700;
    font-size: 33px;
    line-height: 38px;
    letter-spacing: 1.5px;
    color: var(--red);
    text-transform: uppercase;
  }
</style>
</head>
<body>
<div class="sheet">

  <section class="card card--front" aria-label="Business card front">
    <svg class="card__decor" viewBox="0 0 809 473" aria-hidden="true">
      <circle cx="650" cy="236" r="250" fill="var(--red)"/>
    </svg>
    <div class="brand">
      <span class="brand__dot"></span>
      <span class="brand__name">Brindlewood<br>First Aid</span>
    </div>
    <div class="contact">
      <p class="contact__name">Dana Whitfield</p>
      <p class="contact__phone">0491 570 226</p>
      <p class="contact__lines">help@brindlewoodfirstaid.com.au<br>brindlewoodfirstaid.com.au</p>
    </div>
  </section>

  <section class="card card--back" aria-label="Business card back">
    <svg class="card__decor" viewBox="0 0 809 473" aria-hidden="true">
      <circle cx="100" cy="239" r="225" fill="var(--red)"/>
    </svg>
    <div class="offer">
      <p class="offer__title offer__title--red">Onsite Training</p>
      <p class="offer__title offer__title--grey">We can come to you</p>
      <ul class="benefits">
        <li>Time efficient</li>
        <li>Cost effective</li>
        <li>Minimise downtime for your team</li>
      </ul>
      <p class="services">First Aid Training<br>WHS Training</p>
    </div>
  </section>

</div>
</body>
</html>
```